Engineering group involved with fire safety needs a business card

We need a business card design for a company based in Greece called "Voranis Group". We are engineers and specialized technicians, operating the following : a) Fire fighting equipment trade b) Installation , Inspection & Maintenance of fire extinguishers and fire protection systems c) Occupational Health & Safety (Risk assessment & management/ Staff training). We need a clear and simple card design. I uploaded a draft I made, in order to give you an idea of the company and how I currently imagine the design of the card. I also uploaded the logo in .png file format. We are always open to different, new suggestions and ideas you may want to submit.
Target Market(s)
industries, companies, managers, retail clients
Industry/Entity Type
Fire Safety
Contact Information for Business Card
Addresses & phone numbers (headquarters + branch), logo, name (you can find all the details on the uploaded files!)
Colors
Designer to choose colors to be used in the design.
Look and feel
Each slider illustrates characteristics of the customer's brand and the style your logo design should communicate.

```html
<!DOCTYPE html>
<html lang="en">
<head>
<meta charset="utf-8">
<title>Voranis Group – Business Card</title>
<link rel="stylesheet" href="https://fonts.googleapis.com/css2?family=Montserrat:wght@500;600;700&display=swap">
<style>
:root{
  --backdrop:#e6eaea;
  --card:#212528;
  --band:#4a4d4f;
  --red:#e4343a;
  --white:#ffffff;
  --rule:#8a8d90;
}
*{margin:0;padding:0;box-sizing:border-box}
html,body{width:1200px;height:1000px;overflow:hidden}
body{background:var(--backdrop);font-family:"Montserrat",Arial,sans-serif;position:relative}
.card{position:absolute;left:300px;width:601px;background:var(--card);box-shadow:6px 7px 8px rgba(0,0,0,.35);color:var(--white);overflow:hidden}
.card--front{top:116px;height:351px}
.card--back{top:534px;height:350px}

/* front */
.front-name{position:absolute;top:88px;left:0;width:100%;height:46px;display:flex;justify-content:center;align-items:center;gap:14px}
.front-name .mark-square{width:36px;height:36px;background:var(--red)}
.front-name .wordmark{font-weight:700;font-size:34px;line-height:46px;letter-spacing:1px;color:var(--white)}
.services{position:absolute;top:191px;width:100%;text-align:center;list-style:none;font-weight:600;font-size:13.5px;line-height:24.7px;letter-spacing:.2px}
.web-line{position:absolute;top:297px;width:100%;text-align:center;color:var(--red);font-weight:600;font-size:13.5px}
.web-line .sep{margin:0 8px}

/* back */
.back-name{position:absolute;top:86px;left:0;width:100%;height:40px;display:flex;justify-content:center;align-items:center;gap:10px}
.back-name .mark-square{width:28px;height:28px;background:var(--red)}
.back-name .wordmark{font-weight:700;font-size:30px;line-height:40px;color:var(--red);letter-spacing:.5px}
.brand-rule{position:absolute;top:136px;left:0;width:100%;height:2px}
.brand-rule::before,.brand-rule::after{content:"";position:absolute;top:0;height:2px;background:var(--white)}
.brand-rule::before{left:0;width:243px}
.brand-rule::after{right:0;width:243px}
.brand-rule .label{position:absolute;left:0;width:100%;top:-11px;text-align:center;font-weight:700;font-size:19px;line-height:24px;letter-spacing:1.5px}
.tagline{position:absolute;top:157px;width:100%;text-align:center;font-weight:600;font-size:13.5px}
.grey-band{position:absolute;top:193px;left:0;width:100%;height:12px;background:var(--band)}
.red-band{position:absolute;bottom:0;left:0;width:100%;height:17px;background:var(--red)}
.person{position:absolute;top:233px;right:357px;text-align:right}
.person .name{font-weight:600;font-size:18px;letter-spacing:.3px;margin-bottom:4px}
.person .role{color:var(--red);font-weight:500;font-size:13.5px;line-height:16.5px}
.person .email{font-weight:500;font-size:11px;margin-top:6px}
.divider{position:absolute;left:257px;top:216px;width:1px;height:105px;background:var(--rule)}
.contacts{position:absolute;left:270px;top:215px;list-style:none;font-weight:600;font-size:11.8px;line-height:22px}
.contacts .key{color:var(--red)}
</style>
</head>
<body>

<section class="card card--front">
  <div class="front-name">
    <span class="mark-square"></span>
    <span class="wordmark">VORANIS GROUP</span>
  </div>
  <ul class="services">
    <li>FIRE FIGHTING EQUIPMENT</li>
    <li>LICENSING &amp; BUSINESS REGISTRATION</li>
    <li>OCCUPATIONAL HEALTH &amp; SAFETY</li>
    <li>STAFF TRAINING</li>
  </ul>
  <p class="web-line">www.voranisgroup.gr<span class="sep">|</span>info@voranisgroup.gr</p>
</section>

<section class="card card--back">
  <div class="back-name">
    <span class="mark-square"></span>
    <span class="wordmark">VORANIS</span>
  </div>
  <div class="brand-rule"><span class="label">GROUP</span></div>
  <p class="tagline">Installation • Inspection • Maintenance</p>
  <div class="grey-band"></div>

  <div class="person">
    <p class="name">NIKOS ANDRAKIS</p>
    <p class="role">Mechanical Engineer</p>
    <p class="role">OHS Consultant</p>
    <p class="email">nikos.andrakis@voranisgroup.gr</p>
  </div>
  <div class="divider"></div>
  <ul class="contacts">
    <li><span class="key">Tel. (HQ)</span> +30 2292045180</li>
    <li><span class="key">Tel. (BO)</span> +30 210 8091427</li>
    <li><span class="key">Mob.</span> +30 694 512 73 08</li>
    <li><span class="key">Headquarters:</span> 14 Elaion Street, 19400 Keratea</li>
    <li><span class="key">Branch Office:</span> 22 Ippokratous Ave, 15125 Kifisia</li>
  </ul>
  <div class="red-band"></div>
</section>

</body>
</html>
```